Stationary design for real estate company in Trinidad and Tobago

Meridor Realty Ltd. , real estate company operating in Trinidad and Tobago, requires a sleek, modern and professional stationary package to wow our customers and potential new clients. we want to look sleek and professional; first impressions count in this business!
Business Address:
Level 1, Corvane Point Tower
4K Selwick Grove Boulevard
Corvane Point
Halden Pruitt Highway
Port of Spain
Trinidad
Tel: + 1 868 555 0147
www.meridor-tt.example
info@meridor-tt.example

```html
<!DOCTYPE html>
<html lang="en">
<head>
<meta charset="utf-8">
<title>Meridor Realty Ltd. — Business Card</title>
<link rel="stylesheet" href="https://fonts.googleapis.com/css2?family=Montserrat:wght@700&family=Raleway:wght@500&family=Roboto:wght@400&family=Cinzel:wght@400&display=swap">
<style>
  :root {
    --navy: #1e3160;
    --gold: #c7a35f;
    --ink-grey: #6b6b6b;
    --paper: #ffffff;
    --silver: #c9cbe0;
    --backdrop: #e9e9ec;
  }
  * { margin: 0; padding: 0; box-sizing: border-box; }
  html, body { width: 1200px; height: 800px; overflow: hidden; }
  body {
    background: var(--backdrop);
    display: flex;
    align-items: center;
    justify-content: center;
    gap: 40px;
  }
  .card {
    position: relative;
    width: 540px;
    height: 309px;
    box-shadow: 0 6px 18px rgba(0,0,0,0.18);
  }
  .card--front { background: var(--paper); }
  .card--back {
    background: var(--navy);
    display: flex;
    align-items: center;
    justify-content: center;
  }
  .holder { position: absolute; left: 44px; top: 40px; }
  .holder__name {
    font-family: "Montserrat", sans-serif;
    font-weight: 700;
    font-size: 18px;
    letter-spacing: 0.5px;
    color: var(--navy);
    text-transform: uppercase;
  }
  .holder__role {
    font-family: "Raleway", sans-serif;
    font-weight: 500;
    font-size: 16px;
    color: var(--gold);
    margin-top: 2px;
  }
  .contacts {
    position: absolute;
    left: 44px;
    top: 128px;
    list-style: none;
    font-family: "Roboto", sans-serif;
    font-size: 14px;
    color: var(--ink-grey);
  }
  .contacts li { display: flex; align-items: center; gap: 8px; height: 21px; }
  .contacts svg { width: 14px; height: 14px; flex: none; }
  .divider {
    position: absolute;
    left: 44px;
    right: 44px;
    top: 208px;
    height: 1px;
    background: var(--gold);
  }
  .address {
    position: absolute;
    left: 44px;
    top: 220px;
    font-family: "Roboto", sans-serif;
    font-size: 13.5px;
    line-height: 20px;
    color: var(--ink-grey);
    font-style: normal;
  }
  .brand {
    display: flex;
    align-items: center;
    gap: 10px;
  }
  .brand__dot {
    width: 16px;
    height: 16px;
    border-radius: 50%;
    background: var(--gold);
  }
  .brand__name {
    font-family: "Cinzel", serif;
    font-weight: 400;
    letter-spacing: 2px;
  }
  .card--front .brand {
    position: absolute;
    right: 40px;
    top: 110px;
  }
  .card--front .brand__name { font-size: 22px; color: var(--navy); }
  .card--back .brand__name { font-size: 34px; color: var(--silver); }
  .card--back .brand__dot { width: 22px; height: 22px; }
</style>
</head>
<body>
  <section class="card card--front" aria-label="Business card front">
    <div class="holder">
      <h1 class="holder__name">Tobias L. Renwick</h1>
      <p class="holder__role">Founder &amp; CEO</p>
    </div>

    <div class="brand">
      <span class="brand__dot"></span>
      <span class="brand__name">MERIDOR REALTY</span>
    </div>

    <ul class="contacts">
      <li>
        <svg viewBox="0 0 24 24" aria-hidden="true"><path fill="#1e3160" d="M6.6 10.8a15.1 15.1 0 0 0 6.6 6.6l2.2-2.2a1 1 0 0 1 1-.25 11.4 11.4 0 0 0 3.6.57 1 1 0 0 1 1 1V20a1 1 0 0 1-1 1A17 17 0 0 1 3 4a1 1 0 0 1 1-1h3.5a1 1 0 0 1 1 1c0 1.25.2 2.45.57 3.57a1 1 0 0 1-.25 1z"/></svg>
        + 1 868 555 0147
      </li>
      <li>
        <svg viewBox="0 0 24 24" aria-hidden="true"><rect x="2" y="5" width="20" height="14" fill="none" stroke="#1e3160" stroke-width="2"/><path d="M2 5l10 8 10-8" fill="none" stroke="#1e3160" stroke-width="2"/></svg>
        info@meridor-tt.example
      </li>
      <li>
        <svg viewBox="0 0 24 24" aria-hidden="true"><g fill="none" stroke="#1e3160" stroke-width="1.6"><circle cx="12" cy="12" r="10"/><ellipse cx="12" cy="12" rx="4.5" ry="10"/><path d="M2 12h20M4 7h16M4 17h16"/></g></svg>
        www.meridor-tt.example
      </li>
    </ul>

    <div class="divider"></div>

    <address class="address">
      Level 1, Corvane Point Tower 4K Selwick Grove Boulevard<br>
      Corvane Point Halden Pruitt Highway Port of Spain Trinidad
    </address>
  </section>

  <section class="card card--back" aria-label="Business card back">
    <div class="brand">
      <span class="brand__dot"></span>
      <span class="brand__name">MERIDOR REALTY</span>
    </div>
  </section>
</body>
</html>
```